Logo-Design für Oldtimerhandel Wendtner&Wendtner klassische Automobile OG
Zielgruppe
Handel mit Oldtimern, speziell aus den 60er und 70er Jahren. Zielgruppe sind überwiegend Menschen, die sich von der Masse abheben möchten und Wert auf etwas Einzigartiges legen.
Aufgabenstellung
Das Design soll ein hochwertiges Gesamterscheinungsbild mit gutem Wiedererkennungswert haben. Auch kann ein stilisierter Oldtimer Teil des Logos sein, um für die Zielgruppe besser erkennbar zu sein.
Das Logo muss für Homepage, Visitkarten, Briefpapier etc. tauglich sein und auch in S/W gut erkennbar sein können. Ebenso sollte es möglich sein, Autos mit dem Logo bzw. Schriftzug zu branden.
Beispielhaft wäre das Logo bzw. der Internetauftritt von http://www.moravek-vintage-motors.com vergleichbar.

```html
<!DOCTYPE html>
<html lang="de">
<head>
<meta charset="utf-8">
<title>Wendtner &amp; Wendtner – Geschäftsausstattung</title>
<link href="https://fonts.googleapis.com/css2?family=Source+Sans+3:ital,wght@0,400;0,600;1,600;1,700&display=swap" rel="stylesheet">
<style>
:root{
  --bg:#e9e9ea;
  --ink:#1a1a1a;
  --paper:#ffffff;
  --paper-grey:#f1f1f1;
  --red:#d9222a;
  --red-dark:#b81e27;
  --gold:#c9a567;
  --black:#000000;
  --band-grey:#bcbcbc;
}
*{margin:0;padding:0;box-sizing:border-box}
html,body{width:1200px;height:641px;overflow:hidden}
body{background:var(--bg);font-family:"Source Sans 3",sans-serif;color:var(--ink);position:relative}
.item{position:absolute}

/* brand mark: one plain circle with the name set below */
.brand-mark{display:flex;flex-direction:column;align-items:center;justify-content:center;text-align:center}
.brand-mark .dot{border-radius:50%;flex:none}
.brand-mark .name{font-weight:600;line-height:1.1;white-space:nowrap}

/* logo panels */
.panel-black{left:27px;top:123px;width:281px;height:223px;background:var(--black)}
.panel-white{left:27px;top:356px;width:281px;height:222px;background:var(--paper)}
.panel-black .brand-mark,.panel-white .brand-mark{width:100%;height:100%;gap:12px}
.panel-black .dot{width:110px;height:110px;background:var(--paper)}
.panel-black .name{color:var(--paper);font-size:21px}
.panel-white .dot{width:110px;height:110px;background:var(--black)}
.panel-white .name{color:var(--black);font-size:21px}
.logo-gold{left:322px;top:70px;width:195px;height:158px;gap:8px}
.logo-gold .dot{width:104px;height:104px;background:var(--gold)}
.logo-gold .name{font-size:19px;color:var(--ink)}

/* business card */
.card{left:502px;top:233px;width:197px;height:109px;background:var(--paper-grey);overflow:hidden}
.card .company{position:absolute;left:8px;top:7px;font-style:italic;font-weight:600;font-size:8.2px;line-height:10.5px}
.card .band{position:absolute;left:0;top:45px;width:197px;height:12px;background:linear-gradient(90deg,var(--red-dark),var(--red) 60%,#f4a0a3)}
.card .band span{position:absolute;left:14px;top:0;color:var(--paper);font-style:italic;font-weight:700;font-size:8px;line-height:12px}
.card .mini{position:absolute;right:8px;top:8px;width:64px;gap:3px}
.card .mini .dot{width:34px;height:34px;background:var(--gold)}
.card .mini .name{font-size:6px}
.card .foot{position:absolute;top:84px;font-size:5px;line-height:6px}
.card .addr{left:8px}
.card .tel{left:64px;padding-left:6px;border-left:1px solid var(--ink);top:83px}
.card .web{right:7px;text-align:right;top:84px}
.card .corner{position:absolute;right:0;bottom:0;width:74px;height:9px;background:var(--red);clip-path:polygon(14% 0,100% 0,100% 100%,0 100%)}

/* envelope */
.envelope{left:337px;top:368px;width:372px;height:212px;background:var(--paper);border-radius:18px 18px 0 0}
.envelope .flap{position:absolute;left:0;top:0;width:100%;height:45px;border-bottom:1px solid #e2e2e2}
.envelope .sender{position:absolute;left:18px;top:48px}
.envelope .sender .brand-mark{width:64px;gap:2px;margin-left:0}
.envelope .sender .dot{width:34px;height:34px;background:var(--gold)}
.envelope .sender .name{font-size:6.5px}
.envelope .sender .company{margin-top:6px;font-style:italic;font-weight:600;font-size:8.5px;line-height:10.5px}
.envelope .sender .street{font-size:5px;margin-top:2px}
.envelope .to{position:absolute;left:204px;top:118px;font-size:11px}
.envelope .recipient{position:absolute;left:233px;top:121px;width:123px;height:66px;border:1px solid #9a9a9a;border-radius:9px;padding:9px 12px;font-variant:small-caps;letter-spacing:1.2px;font-size:7.5px;line-height:8.5px}
.envelope .recipient .who{font-size:8.5px;margin-bottom:12px}
.envelope .rule{position:absolute;left:0;top:199px;width:239px;height:2px;background:var(--red)}
.envelope .web{position:absolute;left:250px;top:193px;font-size:8.5px}

/* letterhead */
.letterhead{left:743px;top:123px;width:320px;height:450px;background:var(--paper-grey);overflow:hidden}
.letterhead .head-mark{position:absolute;left:16px;top:12px;width:96px;gap:4px}
.letterhead .head-mark .dot{width:62px;height:62px;background:var(--gold)}
.letterhead .head-mark .name{font-size:8px}
.letterhead .contact{position:absolute;right:36px;top:15px;text-align:right;font-size:7.6px;line-height:9.3px}
.letterhead .footer-company{position:absolute;left:58px;top:404px;font-style:italic;font-weight:600;font-size:7px;line-height:9px}
.letterhead .footer-addr{position:absolute;right:10px;top:414px;font-size:5px;text-align:right;line-height:6.6px}
.letterhead .footer-band{position:absolute;left:0;bottom:0;width:100%;height:18px;background:var(--band-grey)}
.letterhead .footer-band .red{position:absolute;left:0;top:0;width:83px;height:18px;background:var(--red);clip-path:polygon(0 0,87% 0,100% 100%,0 100%)}
</style>
</head>
<body>

<section class="item panel-black" aria-label="Logo negativ">
  <div class="brand-mark"><span class="dot"></span><span class="name">Wendtner &amp; Wendtner</span></div>
</section>

<section class="item panel-white" aria-label="Logo positiv">
  <div class="brand-mark"><span class="dot"></span><span class="name">Wendtner &amp; Wendtner</span></div>
</section>

<section class="item logo-gold brand-mark" aria-label="Logo farbig">
  <span class="dot"></span><span class="name">Wendtner &amp; Wendtner</span>
</section>

<section class="item card" aria-label="Visitenkarte">
  <p class="company">Oldtimerhandel<br>Wendtner &amp; Wendtner<br>klassische Automobile OG</p>
  <div class="band"><span>R. Wendtner</span></div>
  <div class="brand-mark mini"><span class="dot"></span><span class="name">Wendtner &amp; Wendtner</span></div>
  <p class="foot addr">Kesselweg 14<br>D- 84028 Landshut<br>Deutschland</p>
  <p class="foot tel">T +49 (0)871 20415<br>T +49 (0)871 20416<br>T +49 (0)171 3820947</p>
  <p class="foot web">email: wendtner-oldtimer.de<br>www.wendtner-oldtimer.de</p>
  <span class="corner"></span>
</section>

<section class="item envelope" aria-label="Briefumschlag">
  <div class="flap"></div>
  <div class="sender">
    <div class="brand-mark"><span class="dot"></span><span class="name">Wendtner &amp; Wendtner</span></div>
    <p class="company">Oldtimerhandel<br>Wendtner &amp; Wendtner<br>klassische Automobile OG</p>
    <p class="street">Kesselweg 14, D- 84028 Landshut, Deutschland</p>
  </div>
  <p class="to">TO:</p>
  <div class="recipient">
    <p class="who">Mr. Brandt</p>
    <p>Lindenhof 3<br>D- 98574 Kleinfeld<br>Croatia</p>
  </div>
  <span class="rule"></span>
  <p class="web">www.wendtner-oldtimer.de</p>
</section>

<section class="item letterhead" aria-label="Briefbogen">
  <div class="brand-mark head-mark"><span class="dot"></span><span class="name">Wendtner &amp; Wendtner</span></div>
  <p class="contact">Kesselweg 14<br>D- 84028 Landshut<br>Tel. +49 (0)871 / 20415<br>Tel. +49 (0)871 / 20416<br>Tel. +49 (0)171 / 3820947<br>email: wendtner-oldtimer.de<br>www.wendtner-oldtimer.de</p>
  <p class="footer-company">Oldtimerhandel Wendtner &amp; Wendtner<br>klassische Automobile OG</p>
  <p class="footer-addr">Kesselweg 14, D- 84028 Landshut, Deutschland<br>IBAN DE12 3456 7890 1234 5678, BIC NRDBDEFFXXX, Nordbank, Steuernummer: 1234/5678</p>
  <div class="footer-band"><span class="red"></span></div>
</section>

</body>
</html>
```